physio rehab flyer for Vela Motion please

Specification:
Flyer is to be trifold from letter size (8.5 x 11)
-----------------------This may help you:--------------------------
I would like the look of :
clean, minimalistic look with mainly blue and green
san serif font
professional
The colors I like are blue (not the blue in the logo enclosed, I want a change, but more like the blue on my website logo) and light green.
This is my website: www.velamotiongroup.ca just so you get an idea but it will be totally changed soon to a to be determined design.
I like the blue and green in file "sample 2" (enclosed)
I like the pictures in "sample 2" file enclosed
For inspiration, I like design of this brochure: http://www.qlx.ca/HarbourRestore/PatientsFamilies/Clinics_Tests/DAWL_Service/Documents/Brochure.pdf
Here's how I see the pages layout:
----[location: this should be the cover (outside, right panel of trifold)]-----
Vela Motion Logo
Integrated Injury Rehab
Evidence-based, one-on-one care to make your recovery fast and comfortable
www.velamotiongroup.ca
---------------[location: inside, left panel]----------------------------------------
Our team leaders
[portrait here]
Harriet Osei, MD, FRCPC, MSC, CIME
Physiatrist
Dr. Osei specializes in injury rehab and sports medicine. She is highly trained having received her MD and Residency in Physiatry from Wexmoor University. Her passion is to help injured people get back to their life.
[portrait here]
Dorothy Varga, PT
Physiotherapist
Dorothy has over 10 years of experience as a Physiotherapist (5 in Canada). She has advanced training in orthopedics and manual therapy. She loves and relates well with people from the youngest to the most senior.
--------------------[location: inside, middle panel]-------------------------------
Our services
We provide integrated assessment and care from interprofessional team of regulated healthcare professionals with proven experience in injury rehabilitation:
physiatrists
sport medicine physicians
physiotherapists
chiropractors
massage therapists
acupuncturists
psychologists
We provide custom medical bracing, orthotics, orthopedic shoes, assistive devices, and medical stockings, all in one place.
----------------------[location: inside, right panel]-----------------------------------
Only registered physiotherapists
We strongly believe in consistency with your treatment plan. This means that you spend your time here one-on-one with your physiotherapist, not any students or assistants. You get consistent high quality care from a professional.
One-on-one attention
We book maximum 3 people per hour to ensure everyone gets adequate one-on-one time with their physiotherapist. This compares favorably with other clinics, who may book upwards of 5-6 per hour. The atmosphere is professional -balanced with friendly, caring and relaxed. Our highly qualified staff operate this way to help make your recovery faster and more enjoyable.
------------------------[location: outside, left panel]---------------------------------
The right rehab for your clients
Timely access to comprehensive assessment and treatment
Proven track record in injury rehabilitation
Convenient one-stop service
Customized treatment plans
Integrated, co-ordinated care
Evidence-based care applying leading best practices
Access to specialty clinics: Physiatry and Chronic Pain
-------------------------[location: outside, middle panel]--------------------------
Please call us 416-738-4062
for more information on injury rehabilitation
Vela Motion Group
8120 Tolliver Rd., Unit 9
Scarborough, ON M4K 8B2
[Please include a line art map designed based on "map" file enclosed]
To make a referral for your clients, contact velamotiongroup@brisklane.ca or fax: 416-738-4059. Thank you.
www.velamotiongroup.ca
------------------------------------------------------------------------------------------------
Target Market(s)
family doctors, ER docs, lawyers, and general public age (20-50)
Industry/Entity Type
Health And Wellness
Requirements
Must have
- san serif font
- blue and green colors
- clean, sophisticated look
Nice to have
- consumer choice award badge either on front or back of trifold
Should not have
- see above

```html
<!DOCTYPE html>
<html lang="en">
<head>
<meta charset="utf-8">
<title>Vela Motion Group – Inside Spread</title>
<link rel="stylesheet" href="https://fonts.googleapis.com/css2?family=Raleway:wght@300;400;500;600;700&display=swap">
<style>
  :root {
    --green: #a9cd3a;
    --green-text: #9bc43b;
    --blue: #2f6fb1;
    --blue-dark: #2a5fa5;
    --blue-soft: #8eadd3;
    --white: #ffffff;
  }
  * { margin: 0; padding: 0; box-sizing: border-box; }
  html, body { width: 1200px; height: 927px; overflow: hidden; background: var(--white); }
  body { font-family: "Raleway", Arial, sans-serif; font-weight: 300; }
  .spread { position: relative; width: 1200px; height: 927px; }
  .panel { position: absolute; top: 0; width: 400px; height: 927px; }
  .panel--team { left: 0; }
  .panel--services { left: 400px; background: var(--green); }
  .panel--care { left: 800px; }

  /* Team */
  .team-title {
    position: absolute; left: 10px; top: 38px; width: 377px; height: 44px;
    background: var(--green); color: var(--white);
    font-size: 34px; line-height: 44px; padding-left: 10px; font-weight: 300;
  }
  .team-title svg { position: absolute; right: 10px; top: 5px; }
  .portrait {
    position: absolute; left: 97px; width: 202px; height: 202px; border-radius: 50%;
    border: 8px solid var(--green);
  }
  .portrait--lead { top: 110px; background: radial-gradient(circle at 50% 45%, #efe7e0 0%, #c9a48a 55%, #7d5a45 100%); }
  .portrait--physio { top: 496px; background: radial-gradient(circle at 50% 45%, #eae6e3 0%, #b88e7a 55%, #8c8fa0 100%); }
  .member-name {
    position: absolute; left: 0; width: 400px; text-align: center;
    color: var(--blue-dark); font-weight: 600; font-size: 18.5px;
  }
  .member-role {
    position: absolute; left: 20px; width: 357px; height: 22px;
  }
  .member-role::before {
    content: ""; position: absolute; left: 0; right: 0; top: 11px; border-top: 1.5px solid var(--green);
  }
  .member-role span {
    position: relative; display: block; margin: 0 auto; width: max-content;
    background: var(--white); border: 1.5px solid var(--green);
    color: var(--blue-dark); font-size: 16px; line-height: 19px; padding: 0 4px;
  }
  .member-bio {
    position: absolute; left: 20px; width: 357px; color: var(--blue-soft);
    font-size: 14.2px; line-height: 18.5px; text-align: justify; text-align-last: center;
  }

  /* Services */
  .services-title {
    position: absolute; left: 20px; top: 38px; font-size: 34px; color: var(--blue-dark); font-weight: 300;
  }
  .services-title-icon { position: absolute; left: 336px; top: 40px; }
  .services-copy {
    position: absolute; left: 20px; width: 356px; color: var(--white);
    font-size: 20.5px; line-height: 25.3px; text-align: justify; font-weight: 400;
  }
  .services-list { position: absolute; left: 20px; top: 284px; width: 356px; list-style: none; }
  .services-list li {
    position: relative; height: 40px; margin-bottom: 24px; background: var(--blue);
    color: var(--white); font-size: 23px; line-height: 40px; padding-left: 59px; font-weight: 400;
  }
  .services-list svg { position: absolute; left: 11px; top: 3px; }

  /* Care */
  .photo { position: absolute; left: 0; width: 400px; }
  .photo--clinician { top: 0; height: 212px; background: linear-gradient(120deg, #d9d4cf 0%, #f2f0ee 45%, #c7c5c4 75%, #8f8b88 100%); }
  .photo--treatment { top: 430px; height: 222px; background: linear-gradient(110deg, #3a2a22 0%, #8a6550 35%, #d8b69c 55%, #5a4438 80%, #2a211d 100%); }
  .care-heading {
    position: absolute; left: 20px; color: var(--green-text); font-weight: 700; font-size: 21px;
  }
  .care-copy {
    position: absolute; left: 20px; width: 358px; color: var(--blue-soft);
    font-size: 16.8px; line-height: 21.9px; text-align: justify;
  }
</style>
</head>
<body>
<main class="spread">

  <section class="panel panel--team">
    <h2 class="team-title">Our Team Leaders
      <svg width="36" height="34" viewBox="0 0 36 34" aria-hidden="true">
        <path d="M16 2c8 0 14 5 14 13 0 3-1 5-2 7v10H14v-5H9c-2 0-3-1-3-3v-4l-3-1 3-6C7 6 11 2 16 2z" fill="none" stroke="#fff" stroke-width="2.5"/>
        <circle cx="18" cy="14" r="4" fill="#fff"/>
      </svg>
    </h2>

    <div class="portrait portrait--lead" role="img" aria-label="Portrait of Dr. Harriet Osei"></div>
    <h3 class="member-name" style="top:323px">Harriet Osei,&nbsp; MD, FRCPC, MSC, CIME</h3>
    <div class="member-role" style="top:353px"><span>Physiatrist</span></div>
    <p class="member-bio" style="top:383px">Dr. Osei specializes in injury rehab and sports medicine. She is highly trained having received her MD and Residency in Physiatry from Wexmoor University. Her passion is to help injured people get back to their life.</p>

    <div class="portrait portrait--physio" role="img" aria-label="Portrait of Dorothy Varga"></div>
    <h3 class="member-name" style="top:712px">Dorothy Varga, PT</h3>
    <div class="member-role" style="top:742px"><span>Physiotherapist</span></div>
    <p class="member-bio" style="top:773px">Dorothy has over 10 years of experience as a Physiotherapist (5 in Canada). She has advanced training in orthopedics and manual therapy. She loves and relates well with people form the youngest to the most senior.</p>
  </section>

  <section class="panel panel--services">
    <h2 class="services-title">Our Services</h2>
    <svg class="services-title-icon" width="42" height="42" viewBox="0 0 42 42" aria-hidden="true">
      <circle cx="21" cy="21" r="20" fill="#2f6fb1"/>
      <text x="21" y="30" text-anchor="middle" font-family="Georgia, serif" font-style="italic" font-weight="700" font-size="26" fill="#a9cd3a">i</text>
    </svg>
    <p class="services-copy" style="top:116px">We provide integrated assessment and care from interprofessional team of regulated healthcare professionals with proven experience in injury rehabilitation:</p>

    <ul class="services-list">
      <li><svg width="36" height="34" viewBox="0 0 36 34" aria-hidden="true"><circle cx="17" cy="17" r="15" fill="none" stroke="#a9cd3a" stroke-width="2.5"/><path d="M10 17l6 6 14-15" fill="none" stroke="#a9cd3a" stroke-width="2.5" stroke-linecap="round" stroke-linejoin="round"/></svg>Physiatrists</li>
      <li><svg width="36" height="34" viewBox="0 0 36 34" aria-hidden="true"><circle cx="17" cy="17" r="15" fill="none" stroke="#a9cd3a" stroke-width="2.5"/><path d="M10 17l6 6 14-15" fill="none" stroke="#a9cd3a" stroke-width="2.5" stroke-linecap="round" stroke-linejoin="round"/></svg>Sport Medicine Physicians</li>
      <li><svg width="36" height="34" viewBox="0 0 36 34" aria-hidden="true"><circle cx="17" cy="17" r="15" fill="none" stroke="#a9cd3a" stroke-width="2.5"/><path d="M10 17l6 6 14-15" fill="none" stroke="#a9cd3a" stroke-width="2.5" stroke-linecap="round" stroke-linejoin="round"/></svg>Physiotherapists</li>
      <li><svg width="36" height="34" viewBox="0 0 36 34" aria-hidden="true"><circle cx="17" cy="17" r="15" fill="none" stroke="#a9cd3a" stroke-width="2.5"/><path d="M10 17l6 6 14-15" fill="none" stroke="#a9cd3a" stroke-width="2.5" stroke-linecap="round" stroke-linejoin="round"/></svg>Chiropractors</li>
      <li><svg width="36" height="34" viewBox="0 0 36 34" aria-hidden="true"><circle cx="17" cy="17" r="15" fill="none" stroke="#a9cd3a" stroke-width="2.5"/><path d="M10 17l6 6 14-15" fill="none" stroke="#a9cd3a" stroke-width="2.5" stroke-linecap="round" stroke-linejoin="round"/></svg>Massage Therapists</li>
      <li><svg width="36" height="34" viewBox="0 0 36 34" aria-hidden="true"><circle cx="17" cy="17" r="15" fill="none" stroke="#a9cd3a" stroke-width="2.5"/><path d="M10 17l6 6 14-15" fill="none" stroke="#a9cd3a" stroke-width="2.5" stroke-linecap="round" stroke-linejoin="round"/></svg>Acupuncturists</li>
      <li><svg width="36" height="34" viewBox="0 0 36 34" aria-hidden="true"><circle cx="17" cy="17" r="15" fill="none" stroke="#a9cd3a" stroke-width="2.5"/><path d="M10 17l6 6 14-15" fill="none" stroke="#a9cd3a" stroke-width="2.5" stroke-linecap="round" stroke-linejoin="round"/></svg>Psychologists</li>
    </ul>

    <p class="services-copy" style="top:750px">We provide custom medical bracing, orthotics, orthopedic shoes, assistive devices, and medical stockings, all in one place.</p>
  </section>

  <section class="panel panel--care">
    <div class="photo photo--clinician" role="img" aria-label="Close-up of a clinician's white coat with stethoscope and pens"></div>
    <h2 class="care-heading" style="top:231px">Only registered Physiotherapists</h2>
    <p class="care-copy" style="top:271px">We strongly believe in consistency with your treatment plan. This means that you spend your time here one-on-one with your physiotherapist, not any students or assistants. You get consistent high quality care from a professional.</p>

    <div class="photo photo--treatment" role="img" aria-label="Physiotherapist's hands treating a patient's knee"></div>
    <h2 class="care-heading" style="top:671px">One-on-One attention</h2>
    <p class="care-copy" style="top:710px">We book maximum 3 people per hour to ensure everyone gets adequate one on one time with their physiotherapist.&nbsp; This compares favorably with other clinics, who may book upwards of 5-6 per hour. The atmosphere is professional -balanced with friendly, caring and relaxed. Our highly qualified staff operate this way to help make your recovery faster and more enjoyable.</p>
  </section>

</main>
</body>
</html>
```